Need a fresh corporate identity for an existing Home Shopping Business in Thailand

We are one of the most active TV home shopping companies in Thailand. We need a fresh looking CI for our corporate, the colours of our corporate are Orange and Grey. We want our customers to see us as professional customer service who help them with their purchases.
The logo can be shown as a whole logo or either half logo but not less than half the logo.
Industry/Entity Type
Shopping
Requirements
Must have
- The logo should be shown at least half the logo or full logo.
Should not have
- The logo should not be shown less than half the logo.

```html
<!DOCTYPE html>
<html lang="en">
<head>
<meta charset="utf-8">
<title>Sukhasiri Letterhead</title>
<link href="https://fonts.googleapis.com/css2?family=PT+Sans:wght@400;700&display=swap" rel="stylesheet">
<style>
  :root {
    --backdrop: #e3dcd5;
    --paper: #f4f4f5;
    --brand-orange: #d9541e;
    --ink-grey: #6b6b6b;
    --mark-faint: #e2e2e4;
  }
  * { margin: 0; padding: 0; box-sizing: border-box; }
  html, body {
    width: 1200px; height: 1000px; overflow: hidden;
    background: var(--backdrop);
    font-family: "PT Sans", sans-serif;
  }
  .canvas { position: relative; width: 1200px; height: 1000px; }
  .sheet {
    position: absolute; top: 185px;
    width: 392px; height: 560px;
    background: var(--paper);
    overflow: hidden;
  }
  .sheet--plain { left: 163px; }
  .sheet--accent { left: 681px; }
  .brand {
    position: absolute; top: 26px; left: 0; right: 0;
    display: flex; flex-direction: column; align-items: center; gap: 6px;
  }
  .brand__dot {
    width: 40px; height: 40px; border-radius: 50%;
    background: var(--brand-orange);
  }
  .brand__name {
    color: var(--brand-orange); font-size: 10px; font-weight: 400;
  }
  .corner-shape {
    position: absolute; right: -70px; bottom: -60px;
    width: 230px; height: 230px; border-radius: 50%;
    background: var(--mark-faint);
  }
  .footer {
    position: absolute; left: 24px; right: 24px; top: 502px;
    border-top: 1px solid var(--brand-orange);
    padding-top: 6px;
    display: grid; grid-template-columns: 186px 78px 1fr;
    font-size: 5.2px; line-height: 7.4px; color: var(--ink-grey);
  }
  .footer__company {
    color: var(--brand-orange); font-weight: 700; font-size: 7.5px;
    line-height: 10px; grid-column: 1 / -1;
  }
  .footer__label { color: var(--brand-orange); font-weight: 700; }
</style>
</head>
<body>
<main class="canvas">
  <section class="sheet sheet--plain">
    <header class="brand">
      <span class="brand__dot"></span>
      <span class="brand__name">Sukhasiri</span>
    </header>
    <footer class="footer">
      <p class="footer__company">Lotus Bay Trading Ltd.</p>
      <p class="footer__address">Company No. 2207/118 Riverside Commerce Tower, 3rd Floor,<br>Soi Charoen Nakhon 14, Klong San Rd., Bangkok 10600.</p>
      <p class="footer__phones"><span class="footer__label">T:</span> 02-418-3360<br><span class="footer__label">F:</span> 02-418-3361</p>
      <p class="footer__web"><span class="footer__label">E:</span> hello@sukhasiri.co<br><span class="footer__label">W:</span> www.sukhasirishop.co</p>
    </footer>
  </section>

  <section class="sheet sheet--accent">
    <div class="corner-shape" role="img" aria-label="Faint brand shape in the lower corner"></div>
    <header class="brand">
      <span class="brand__dot"></span>
      <span class="brand__name">Sukhasiri</span>
    </header>
    <footer class="footer">
      <p class="footer__company">Lotus Bay Trading Ltd.</p>
      <p class="footer__address">Company No. 2207/118 Riverside Commerce Tower, 3rd Floor,<br>Soi Charoen Nakhon 14, Klong San Rd., Bangkok 10600.</p>
      <p class="footer__phones"><span class="footer__label">T:</span> 02-418-3360<br><span class="footer__label">F:</span> 02-418-3361</p>
      <p class="footer__web"><span class="footer__label">E:</span> hello@sukhasiri.co<br><span class="footer__label">W:</span> www.sukhasirishop.co</p>
    </footer>
  </section>
</main>
</body>
</html>
```